Institutional website for an IT Consulting company

Web design + HTML + CSS / Bootstrap + JS (interaction) integration in order to extend our existing website brightvale.coop.
Our website is currently aiming only for recruitment and not for customers, we want to provide a fluid transition between customer side website (this project) and recruitment website (existing site).

Ideally we would love the new design to be "inspired" by our actual graphic chart (Colors mainly). It should provide a great user experience and a landing page (or any mean) allowing the visitor to easily switch from the end customer front end (this project), the recruitment front end (existing front end https://www.brightvale.coop/) and the existing member front end (an other existing front end dedicated to members already existing).

In attachment you will find the expected site content mainly a one page with a first level of information and "link" to sub pages (a way to directly access this sub pages should also be provided).

The website should be accessible on mobile device and desktop.

The attachment is in french as it reflect the final site content, but if google translate isn't sufficient to have a general idea of the content, feel free to ask. We would love to have some visual representation for some categories.

Target Market(s)

fortune 500 companies

Industry/Entity Type

It Company

Coding

Coded - Design and coding required

Number of Pages Required

5+ page

Requirements
Must have
• This project must have an easy way to navigate between 3 sub sites, the customer one (the one designed here), the consultant / recruitment one (the existing one at brightvale.coop), the members one.

A one page experience at first leading to detail pages.

Custom made visuals to illustrate each categories.

Inspiration websites : quorb[.]fr ; tasknest[.]com ; dovrally[.] com ...

Be inspired by the existing color from our logo and existing website at brightvale[.]coop

```html
<!DOCTYPE html>
<html lang="en">
<head>
<meta charset="utf-8">
<title>Brightvale.coop</title>
<link rel="stylesheet" href="https://fonts.googleapis.com/css2?family=Libre+Baskerville:wght@400;700&family=Open+Sans:wght@300;400;600&family=Montserrat:wght@400&display=swap">
<style>
:root{
  --ink:#12393a;
  --teal:#2aa6ad;
  --text:#555b5d;
  --muted:#7a7f80;
  --white:#ffffff;
  --black:#000000;
}
*{margin:0;padding:0;box-sizing:border-box}
html,body{width:1200px;height:3043px;overflow:hidden}
body{font-family:"Open Sans",sans-serif;color:var(--text);background:var(--white);position:relative}
a{color:inherit;text-decoration:none}

.topbar{height:46px;background:var(--ink);color:var(--white);font-size:17px;display:flex;justify-content:space-between;align-items:center;padding:0 111px 0 113px}
.topbar .contact{display:flex;align-items:center;gap:6px}
.site-switch{display:flex;gap:4px;font-size:13px}
.site-switch a{padding:3px 12px;border:1px solid rgba(255,255,255,.35);border-radius:12px;color:rgba(255,255,255,.85)}
.site-switch a.current{background:var(--white);color:var(--ink);border-color:var(--white)}

.header{height:84px;display:flex;justify-content:space-between;align-items:center;padding:0 111px}
.brand{font-weight:600;font-size:32px;color:var(--ink);display:flex;align-items:center;gap:8px;letter-spacing:.5px}
.brand-dot{width:14px;height:14px;background:var(--teal)}
.nav{display:flex;gap:24px;font-size:16px;color:#222}
.nav a{padding-bottom:6px}
.nav a.active{color:var(--ink);border-bottom:2px solid var(--ink)}

.hero{position:relative;height:551px;background:linear-gradient(90deg,#eaecea,#f3f4f2 60%);overflow:hidden}
.hero-photo{position:absolute;inset:0}
.hero-content{position:absolute;left:111px;top:130px;width:440px}
.hero h1{font-family:"Libre Baskerville",serif;font-size:56px;font-weight:400;color:var(--ink);letter-spacing:-.5px}
.hero p{font-size:17px;line-height:26px;margin-top:22px;color:#4a4f50}
.btn-dark{display:inline-block;margin-top:26px;background:var(--ink);color:var(--white);font-family:"Libre Baskerville",serif;font-size:18px;height:58px;line-height:58px;width:159px;text-align:center;border-radius:4px}
.play{position:absolute;left:557px;top:240px}

.section-title{font-family:"Libre Baskerville",serif;font-weight:700;font-size:38px;line-height:48px;color:var(--ink);text-align:center;letter-spacing:-.5px}
.zig{display:block;margin:0 auto}

.why{padding-top:85px;height:878px}
.why .zig{margin-top:18px}
.cards{display:grid;grid-template-columns:repeat(3,310px);gap:22px 24px;justify-content:center;margin-top:27px}
.card{height:281px;background:var(--white);box-shadow:0 0 8px rgba(0,0,0,.18);text-align:center;padding-top:24px}
.card .icon{height:88px;display:flex;justify-content:center;align-items:center}
.card .zig{margin-top:28px}
.card p{font-size:17px;line-height:26px;color:var(--muted);font-weight:300;margin:26px auto 0;width:236px}

.about{position:relative;height:474px;background:var(--ink);color:var(--white);text-align:center}
.about-photo{position:absolute;inset:0;background:linear-gradient(100deg,#1d4a4b 0%,#173f41 30%,#12393a 60%,#184244 100%)}
.about-inner{position:relative;padding-top:85px}
.about .section-title{color:var(--white);font-weight:400}
.about .zig{margin-top:18px}
.about p{font-size:17px;line-height:26px;width:860px;margin:26px auto 0}
.btn-light{display:inline-block;margin-top:36px;background:var(--white);color:var(--ink);font-family:"Libre Baskerville",serif;font-size:18px;height:52px;line-height:52px;width:157px;border-radius:4px}

.revenues{padding-top:82px;height:633px}
.revenues .zig{margin-top:18px}
.rev-grid{display:grid;grid-template-columns:repeat(4,234px);gap:14px;justify-content:center;margin-top:34px}
.rev-card{height:289px;box-shadow:0 0 8px rgba(0,0,0,.15);text-align:center}
.rev-card h3{height:67px;line-height:67px;background:var(--ink);color:var(--white);font-family:"Libre Baskerville",serif;font-size:14px;font-weight:400;text-transform:uppercase}
.rev-card .amount{font-family:"Libre Baskerville",serif;font-size:24px;color:var(--ink);margin-top:14px}
.rev-card p{font-size:13px;line-height:25.7px;color:var(--muted);font-weight:300;width:166px;margin:4px auto 0}
.more{display:block;width:130px;margin:36px auto 0;text-align:center;font-family:"Libre Baskerville",serif;font-size:14px;color:var(--ink);text-decoration:underline}

.footer{position:absolute;left:0;top:2666px;width:1200px;height:377px;background:var(--black);color:var(--white);text-align:center}
.footer .brand{justify-content:center;color:var(--teal);margin-top:92px;font-size:34px}
.footer-nav{display:flex;justify-content:center;gap:27px;font-size:18px;font-weight:600;margin-top:32px}
.footer-contact{display:grid;grid-template-columns:repeat(3,300px);justify-content:center;margin-top:20px;font-size:17px;line-height:26px}
.footer-contact span{display:flex;justify-content:center;align-items:flex-start;gap:10px}
.copy{font-family:"Montserrat",sans-serif;font-size:17px;margin-top:24px}
</style>
</head>
<body>

<div class="topbar">
  <span class="contact"><svg width="13" height="13" viewBox="0 0 24 24" fill="#fff"><path d="M6.6 10.8a15 15 0 006.6 6.6l2.2-2.2c.3-.3.7-.4 1-.2 1.1.4 2.3.6 3.6.6.6 0 1 .4 1 1V20c0 .6-.4 1-1 1A17 17 0 013 4c0-.6.4-1 1-1h3.5c.6 0 1 .4 1 1 0 1.3.2 2.5.6 3.6.1.3 0 .7-.2 1z"/></svg>01 45 67 20 18</span>
  <nav class="site-switch" aria-label="Switch site">
    <a class="current" href="#">Clients</a>
    <a href="https://www.brightvale.coop/">Consultants</a>
    <a href="#">Members</a>
  </nav>
  <span class="contact"><svg width="16" height="13" viewBox="0 0 24 18" fill="#fff"><path d="M0 2l12 8 12-8V0H0zM0 4v14h24V4l-12 8z"/></svg>info@brightvale.coop</span>
</div>

<header class="header">
  <a class="brand" href="#"><span>BRIGHTVALE</span><span class="brand-dot"></span></a>
  <nav class="nav">
    <a class="active" href="#">Profile search</a>
    <a href="#">I am Brightvale</a>
    <a href="#">I want to join brightvale</a>
    <a href="#">Contact Us</a>
  </nav>
</header>

<section class="hero">
  <svg class="hero-photo" width="1200" height="551" role="img" aria-label="Photo of two colleagues in a bright office looking at a tablet">
    <defs>
      <linearGradient id="heroPhoto" x1="0" y1="0" x2="1" y2="1">
        <stop offset="0" stop-color="#e6e3df"/>
        <stop offset=".45" stop-color="#c9b9a8"/>
        <stop offset=".75" stop-color="#3c4656"/>
        <stop offset="1" stop-color="#1f2a3d"/>
      </linearGradient>
    </defs>
    <path d="M640 0H1200V551H1020C930 540 850 500 790 430C690 330 578 260 578 150C578 80 600 30 640 0Z" fill="url(#heroPhoto)"/>
  </svg>
  <div class="hero-content">
    <h1>Brightvale.coop</h1>
    <p>BRIGHTVALE.COOP is a cooperative and participatory company specializing in digital services.</p>
    <a class="btn-dark" href="#">Get Started</a>
  </div>
  <svg class="play" width="111" height="111" viewBox="0 0 111 111">
    <circle cx="55.5" cy="55.5" r="55.5" fill="#12393a" fill-opacity=".55"/>
    <circle cx="55.5" cy="55.5" r="40" fill="#12393a"/>
    <circle cx="55.5" cy="55.5" r="23" fill="none" stroke="#fff" stroke-width="3"/>
    <path d="M49 45v21l17-10.5z" fill="#fff"/>
  </svg>
</section>

<section class="why">
  <h2 class="section-title">WHY JOIN US?</h2>
  <svg class="zig" width="99" height="10" viewBox="0 0 99 10"><polyline points="0,9 5.5,1 11,9 16.5,1 22,9 27.5,1 33,9 38.5,1 44,9 49.5,1 55,9 60.5,1 66,9 71.5,1 77,9 82.5,1 88,9 93.5,1 99,9" fill="none" stroke="#2aa6ad" stroke-width="1.3"/></svg>
  <div class="cards">
    <div class="card">
      <div class="icon"><svg width="72" height="86" viewBox="0 0 72 86" fill="none" stroke="#12393a" stroke-width="2.5" stroke-linejoin="round"><rect x="6" y="20" width="18" height="40"/><rect x="24" y="6" width="16" height="54"/><rect x="40" y="24" width="20" height="36"/><path d="M10 30h10M10 40h10M10 50h10M28 16h8M28 26h8M28 36h8M28 46h8M44 34h12M44 44h12"/><path d="M2 66h20l14 6 24-8c4-1 8 3 4 6L40 82H2"/></svg></div>
      <svg class="zig" width="99" height="10" viewBox="0 0 99 10"><polyline points="0,9 5.5,1 11,9 16.5,1 22,9 27.5,1 33,9 38.5,1 44,9 49.5,1 55,9 60.5,1 66,9 71.5,1 77,9 82.5,1 88,9 93.5,1 99,9" fill="none" stroke="#2aa6ad" stroke-width="1.3"/></svg>
      <p>For the equality of statutes and fairness in the valuation of work.</p>
    </div>
    <div class="card">
      <div class="icon"><svg width="68" height="66" viewBox="0 0 68 66" fill="none" stroke="#12393a" stroke-width="5"><circle cx="54" cy="10" r="8"/><circle cx="12" cy="33" r="8"/><circle cx="54" cy="56" r="8"/><path d="M19 29l28-15M19 37l28 15"/></svg></div>
      <svg class="zig" width="99" height="10" viewBox="0 0 99 10"><polyline points="0,9 5.5,1 11,9 16.5,1 22,9 27.5,1 33,9 38.5,1 44,9 49.5,1 55,9 60.5,1 66,9 71.5,1 77,9 82.5,1 88,9 93.5,1 99,9" fill="none" stroke="#2aa6ad" stroke-width="1.3"/></svg>
      <p>For the democratic mode of operation based on the principle of social</p>
    </div>
    <div class="card">
      <div class="icon"><svg width="66" height="66" viewBox="0 0 66 66" fill="none" stroke="#12393a" stroke-width="2.5"><path d="M4 20C14 4 52 4 62 20C52 36 14 36 4 20Z"/><circle cx="33" cy="17" r="8"/><path d="M23 32c2-6 18-6 20 0M33 36v8M12 44h42M12 44v4M33 44v4M54 44v4"/><rect x="6" y="48" width="12" height="14"/><rect x="27" y="48" width="12" height="14"/><rect x="48" y="48" width="12" height="14"/></svg></div>
      <svg class="zig" width="99" height="10" viewBox="0 0 99 10"><polyline points="0,9 5.5,1 11,9 16.5,1 22,9 27.5,1 33,9 38.5,1 44,9 49.5,1 55,9 60.5,1 66,9 71.5,1 77,9 82.5,1 88,9 93.5,1 99,9" fill="none" stroke="#2aa6ad" stroke-width="1.3"/></svg>
      <p>For the cooperative legal framework that reconciles the advantages of employee</p>
    </div>
    <div class="card">
      <div class="icon"><svg width="112" height="70" viewBox="0 0 112 70" fill="none" stroke="#12393a" stroke-width="3.5"><circle cx="56" cy="18" r="14"/><circle cx="26" cy="24" r="11"/><circle cx="86" cy="24" r="11"/><path d="M4 60c0-14 10-22 22-22 6 0 10 2 13 4M108 60c0-14-10-22-22-22-6 0-10 2-13 4M30 66c0-18 12-28 26-28s26 10 26 28c0 2-2 3-4 3H34c-2 0-4-1-4-3zM4 60c0 1 1 2 3 2h20M108 60c0 1-1 2-3 2H85"/></svg></div>
      <svg class="zig" width="99" height="10" viewBox="0 0 99 10"><polyline points="0,9 5.5,1 11,9 16.5,1 22,9 27.5,1 33,9 38.5,1 44,9 49.5,1 55,9 60.5,1 66,9 71.5,1 77,9 82.5,1 88,9 93.5,1 99,9" fill="none" stroke="#2aa6ad" stroke-width="1.3"/></svg>
      <p>For the sharing of knowledge and mutual aid within a group of recognized experts</p>
    </div>
    <div class="card">
      <div class="icon"><svg width="70" height="82" viewBox="0 0 70 82" fill="none" stroke="#12393a" stroke-width="2.5"><path d="M35 2v6M8 14l5 4M62 14l-5 4M2 38h6M62 38h6"/><path d="M35 14c-14 0-24 10-24 23 0 8 4 13 9 18 3 3 4 6 4 10h22c0-4 1-7 4-10 5-5 9-10 9-18 0-13-10-23-24-23z"/><circle cx="35" cy="33" r="7"/><path d="M23 53c2-8 22-8 24 0M26 70h18M28 76h14"/></svg></div>
      <svg class="zig" width="99" height="10" viewBox="0 0 99 10"><polyline points="0,9 5.5,1 11,9 16.5,1 22,9 27.5,1 33,9 38.5,1 44,9 49.5,1 55,9 60.5,1 66,9 71.5,1 77,9 82.5,1 88,9 93.5,1 99,9" fill="none" stroke="#2aa6ad" stroke-width="1.3"/></svg>
      <p>To contribute to the creation of a new model of entrepreneurship facing</p>
    </div>
    <div class="card">
      <div class="icon"><svg width="76" height="76" viewBox="0 0 76 76" fill="none" stroke="#12393a" stroke-width="4"><circle cx="38" cy="38" r="34"/><ellipse cx="38" cy="38" rx="15" ry="34"/><path d="M38 4v68M4 38h68M9 21h58M9 55h58"/></svg></div>
      <svg class="zig" width="99" height="10" viewBox="0 0 99 10"><polyline points="0,9 5.5,1 11,9 16.5,1 22,9 27.5,1 33,9 38.5,1 44,9 49.5,1 55,9 60.5,1 66,9 71.5,1 77,9 82.5,1 88,9 93.5,1 99,9" fill="none" stroke="#2aa6ad" stroke-width="1.3"/></svg>
      <p>To co-construct the digital world of tomorrow with a mode of shared governance.</p>
    </div>
  </div>
</section>

<section class="about">
  <div class="about-photo" role="img" aria-label="Faded photo of hands working with digital network graphics"></div>
  <div class="about-inner">
    <h2 class="section-title">ABOUT US</h2>
    <svg class="zig" width="99" height="10" viewBox="0 0 99 10"><polyline points="0,9 5.5,1 11,9 16.5,1 22,9 27.5,1 33,9 38.5,1 44,9 49.5,1 55,9 60.5,1 66,9 71.5,1 77,9 82.5,1 88,9 93.5,1 99,9" fill="none" stroke="#2aa6ad" stroke-width="1.3"/></svg>
    <p>Lorem ipsum dolor sit amet, consectetur adipiscing elit, sed do eiusmod tempor incididunt ut labore et dolore magna aliqua. Ut enim ad minim veniam, quis nostrud exercitation ullamco laboris nisi ut aliquip ex ea commodo consequat. Duis aute irure dolor in reprehenderit in voluptate velit esse cillum dolore eu fugiat nulla pariatur. Excepteur sint occaecat cupidatat non</p>
    <a class="btn-light" href="#">Learn More</a>
  </div>
</section>

<section class="revenues">
  <h2 class="section-title">SIMULATE YOUR REVENUES</h2>
  <svg class="zig" width="99" height="10" viewBox="0 0 99 10"><polyline points="0,9 5.5,1 11,9 16.5,1 22,9 27.5,1 33,9 38.5,1 44,9 49.5,1 55,9 60.5,1 66,9 71.5,1 77,9 82.5,1 88,9 93.5,1 99,9" fill="none" stroke="#2aa6ad" stroke-width="1.3"/></svg>
  <div class="rev-grid">
    <div class="rev-card"><h3>Monthly net salary</h3><div class="amount">€ 3,481</div><p>Lorem ipsum dolor sit amet, consectetur adipiscing elit, sed do eiusmod tempor incididunt amet, consectetur adipiscing elit, sed do</p></div>
    <div class="rev-card"><h3>Incentive bonus</h3><div class="amount">€ 20,000</div><p>Lorem ipsum dolor sit amet, consectetur adipiscing elit, sed do eiusmod tempor incididunt amet, consectetur adipiscing elit, sed do</p></div>
    <div class="rev-card"><h3>Participation bonus</h3><div class="amount">€ 7,161</div><p>Lorem ipsum dolor sit amet, consectetur adipiscing elit, sed do eiusmod tempor incididunt amet, consectetur adipiscing elit, sed do</p></div>
    <div class="rev-card"><h3>Annual gross income</h3><div class="amount">€ 80,713</div><p>Lorem ipsum dolor sit amet, consectetur adipiscing elit, sed do eiusmod tempor incididunt amet, consectetur adipiscing elit, sed do</p></div>
  </div>
  <a class="more" href="#">View More Details</a>
</section>

<footer class="footer">
  <div class="brand"><span>BRIGHTVALE</span><span class="brand-dot"></span></div>
  <nav class="footer-nav">
    <a href="#">Profile search</a>
    <a href="#">I am Brightvale</a>
    <a href="#">I want to join brightvale</a>
    <a href="#">Contact Us</a>
  </nav>
  <div class="footer-contact">
    <span><svg width="18" height="14" viewBox="0 0 24 18" fill="#fff" style="margin-top:6px"><path d="M0 2l12 8 12-8V0H0zM0 4v14h24V4l-12 8z"/></svg>info@brightvale.coop</span>
    <span><svg width="11" height="16" viewBox="0 0 12 18" fill="#fff" style="margin-top:5px"><path d="M6 0a6 6 0 00-6 6c0 5 6 12 6 12s6-7 6-12a6 6 0 00-6-6zm0 8.5A2.5 2.5 0 116 3.5a2.5 2.5 0 010 5z"/></svg>24 Rue des Lilas<br>75011 Paris</span>
    <span><svg width="14" height="14" viewBox="0 0 24 24" fill="#fff" style="margin-top:6px"><path d="M6.6 10.8a15 15 0 006.6 6.6l2.2-2.2c.3-.3.7-.4 1-.2 1.1.4 2.3.6 3.6.6.6 0 1 .4 1 1V20c0 .6-.4 1-1 1A17 17 0 013 4c0-.6.4-1 1-1h3.5c.6 0 1 .4 1 1 0 1.3.2 2.5.6 3.6.1.3 0 .7-.2 1z"/></svg>01 45 67 20 18</span>
  </div>
  <p class="copy">© Copyrights 2020 &nbsp;Brightvale.Coop &nbsp;| &nbsp;All Rights Reserved</p>
</footer>

</body>
</html>
```